Corvani-Lasch: What Sets Us Apart

My client wants a brochure design (8.5 x 11 folds to 5.5 x 8.5) for their orthodontia practice. Attached is what they currently produce in-house. In my client's request to me: "We want to change this document into a bi-fold brochure that is colorful and attractive and easy to read…bigger, more colorful font, colored paper? We also want to add our contact information. We are completely open to your artistic ideas on how to do this. Let me know your thoughts. Patients/parents take this home with them if they leave our office “uncommitted” to starting treatment and state they will call us back. It needs to be the tool that we hope will help them choose us and call back to schedule." I really do not want 50 designs back. I might want to look at 3 or 5, unless those all are just plain ugly. The text my client wants is attached. I can upload two other pieces they currently use and their logo if I choose to move forward.

```html
<!DOCTYPE html>
<html lang="en">
<head>
<meta charset="utf-8">
<title>Corvani-Lasch — What Sets Us Apart</title>
<link rel="stylesheet" href="https://fonts.googleapis.com/css2?family=Montserrat:wght@300;400;600;700;800&family=Open+Sans:wght@400;600;700&display=swap">
<style>
  :root{
    --bg:#e4e6e8;
    --paper:#ffffff;
    --ink:#1f2a30;
    --ink-blue:#1c6a8c;
    --teal:#27c0ad;
    --aqua:#5fd0dc;
    --mist:#e4f2f7;
    --mist-2:#cfe8f1;
    --deep:#0d4c5c;
    --body:#5b6870;
    --soft:#8fa2ab;
  }
  *{box-sizing:border-box;margin:0;padding:0}
  html,body{width:1200px;height:2250px;overflow:hidden}
  body{background:var(--bg);font-family:"Open Sans",Arial,sans-serif;position:relative}

  .page{position:absolute;width:560px;height:866px;background:var(--paper);overflow:hidden;box-shadow:0 10px 30px rgba(0,0,0,.14)}
  .page svg.art{position:absolute;inset:0;width:100%;height:100%}

  .front-cover{left:25px;top:222px}
  .back-cover{left:615px;top:222px}

  .brand{position:absolute;display:flex;align-items:center;gap:8px;font-family:"Montserrat",Arial,sans-serif;font-weight:700;color:var(--ink);letter-spacing:.14em;text-transform:uppercase}
  .brand__mark{width:14px;height:14px;background:var(--ink)}
  .front-cover .brand{left:0;right:0;top:48px;justify-content:center;font-size:18px}

  .cover-title{position:absolute;right:54px;top:690px;text-align:left;font-family:"Montserrat",Arial,sans-serif;line-height:.98;font-size:52px;letter-spacing:.01em}
  .cover-title__strong{display:block;font-weight:800;color:var(--ink-blue)}
  .cover-title__light{display:block;font-weight:300;color:var(--aqua)}
  .cover-url{position:absolute;right:60px;top:812px;font-size:13px;color:var(--soft);letter-spacing:.04em}

  .back-cover .brand{left:44px;top:690px;font-size:13px;flex-direction:column;align-items:flex-start;gap:6px;width:120px}
  .contact-list{position:absolute;left:190px;top:678px;list-style:none;font-size:14px;color:var(--ink);line-height:1.95}
  .contact-list li{display:flex;align-items:center;gap:10px}
  .contact-list li::before{content:"";width:7px;height:7px;border-radius:50%;background:var(--teal);flex:none}

  .inner-spread{position:absolute;left:40px;top:1162px;width:1120px;height:866px}
  .inner-left{left:0;top:0}
  .inner-right{left:560px;top:0}
  .fold-shadow{position:absolute;left:530px;top:0;width:60px;height:866px;background:linear-gradient(90deg,rgba(0,0,0,0) 0%,rgba(0,0,0,.08) 50%,rgba(0,0,0,0) 100%);pointer-events:none}

  .reason-list{position:absolute;left:48px;right:44px;list-style:none}
  .inner-left .reason-list{top:70px}
  .inner-right .reason-list{top:46px}
  .reason{display:grid;grid-template-columns:40px 1fr;column-gap:12px;margin-bottom:26px}
  .inner-right .reason{margin-bottom:20px}
  .reason__num{width:34px;height:34px;border-radius:50%;border:3px solid var(--teal);background:var(--paper);display:flex;align-items:center;justify-content:center;font-family:"Montserrat",Arial,sans-serif;font-weight:700;font-size:16px;color:var(--ink)}
  .reason__title{font-family:"Montserrat",Arial,sans-serif;font-weight:700;font-size:15px;letter-spacing:.05em;text-transform:uppercase;color:var(--ink-blue);line-height:1.25;padding-top:7px}
  .reason__text{grid-column:1 / span 2;margin-top:8px;font-size:11.5px;line-height:1.55;color:var(--body)}
  .reason__text strong{color:var(--ink);font-weight:700}
</style>
</head>
<body>

<!-- Front cover -->
<section class="page front-cover">
  <svg class="art" viewBox="0 0 560 866" preserveAspectRatio="none">
    <defs>
      <linearGradient id="front-sky" x1="0" y1="0" x2="1" y2="1">
        <stop offset="0" stop-color="#cfe8f1"/>
        <stop offset=".55" stop-color="#eef7fa"/>
        <stop offset="1" stop-color="#ffffff"/>
      </linearGradient>
      <linearGradient id="front-photo" x1="0" y1="0" x2="1" y2="1">
        <stop offset="0" stop-color="#d9eef4"/>
        <stop offset=".5" stop-color="#b9dbe6"/>
        <stop offset="1" stop-color="#e8f4f7"/>
      </linearGradient>
      <linearGradient id="front-band" x1="0" y1="0" x2="1" y2="0">
        <stop offset="0" stop-color="#1faf9e"/>
        <stop offset="1" stop-color="#5fd0dc"/>
      </linearGradient>
      <linearGradient id="front-foot" x1="0" y1="0" x2="0" y2="1">
        <stop offset="0" stop-color="#ffffff"/>
        <stop offset="1" stop-color="#eef6f9"/>
      </linearGradient>
    </defs>
    <rect width="560" height="866" fill="url(#front-foot)"/>
    <polygon points="0,0 560,0 560,190 0,258" fill="url(#front-sky)"/>
    <polygon points="0,262 560,194 560,610 0,672" fill="url(#front-photo)" role="img" aria-label="Photo of a smiling dental assistant holding a model of teeth"/>
    <polygon points="0,252 560,184 560,194 0,262" fill="url(#front-band)"/>
    <polygon points="0,672 560,610 560,622 0,686" fill="url(#front-band)"/>
    <rect x="552" y="0" width="8" height="866" fill="url(#front-band)"/>
  </svg>
  <div class="brand"><span class="brand__mark"></span>Corvani-Lasch</div>
  <h1 class="cover-title">
    <span class="cover-title__strong">WHAT SETS</span>
    <span class="cover-title__light">US APART</span>
  </h1>
  <p class="cover-url">www.corvanilasch-ortho.com</p>
</section>

<!-- Back cover -->
<section class="page back-cover">
  <svg class="art" viewBox="0 0 560 866" preserveAspectRatio="none">
    <defs>
      <linearGradient id="back-sky" x1="0" y1="0" x2="1" y2="1">
        <stop offset="0" stop-color="#ffffff"/>
        <stop offset=".6" stop-color="#e6f3f8"/>
        <stop offset="1" stop-color="#cfe8f1"/>
      </linearGradient>
      <linearGradient id="back-photo" x1="0" y1="0" x2="1" y2="1">
        <stop offset="0" stop-color="#0b3d4c"/>
        <stop offset=".5" stop-color="#136577"/>
        <stop offset="1" stop-color="#2a8aa0"/>
      </linearGradient>
      <linearGradient id="back-band" x1="0" y1="0" x2="1" y2="0">
        <stop offset="0" stop-color="#1faf9e"/>
        <stop offset="1" stop-color="#5fd0dc"/>
      </linearGradient>
      <linearGradient id="back-foot" x1="0" y1="0" x2="1" y2="1">
        <stop offset="0" stop-color="#e6f3f8"/>
        <stop offset=".5" stop-color="#ffffff"/>
        <stop offset="1" stop-color="#ffffff"/>
      </linearGradient>
    </defs>
    <rect width="560" height="866" fill="url(#back-foot)"/>
    <polygon points="0,0 560,0 560,110 0,172" fill="url(#back-sky)"/>
    <polygon points="0,176 560,114 560,560 0,624" fill="url(#back-photo)" role="img" aria-label="Photo of a smiling patient during a dental check-up"/>
    <polygon points="0,624 560,560 560,574 0,640" fill="url(#back-band)"/>
  </svg>
  <div class="brand"><span class="brand__mark"></span>Corvani-Lasch</div>
  <ul class="contact-list">
    <li>+1 555 014 2290</li>
    <li>www.corvanilasch-ortho.com</li>
    <li>hello@corvanilasch-ortho.com</li>
    <li>218 Alder Row, Harlow, 44120</li>
  </ul>
</section>

<!-- Inner spread -->
<section class="inner-spread">
  <div class="page inner-left">
    <svg class="art" viewBox="0 0 560 866" preserveAspectRatio="none">
      <defs>
        <radialGradient id="left-glow" cx="0" cy="0" r="1">
          <stop offset="0" stop-color="#bfe2ec"/>
          <stop offset=".5" stop-color="#e6f3f8"/>
          <stop offset="1" stop-color="#ffffff"/>
        </radialGradient>
      </defs>
      <rect width="560" height="866" fill="url(#left-glow)"/>
    </svg>
    <ol class="reason-list">
      <li class="reason">
        <span class="reason__num">1</span>
        <h2 class="reason__title">Orthodontic Specialists</h2>
        <p class="reason__text">Consider the times you have required the expertise of a specialist for other health concerns. Dr. Corvani &amp; Dr. Lasch are orthodontic specialists. This means they completed 2–3 additional years of full-time orthodontic training beyond dental school. When you choose our doctors, you are placing yourself and your family in the competent hands of TWO orthodontic specialists who will help you achieve the best possible result.</p>
      </li>
      <li class="reason">
        <span class="reason__num">2</span>
        <h2 class="reason__title">Board Certified</h2>
        <p class="reason__text">To become board certified, both doctors had to independently pass a rigorous set of written and clinical examinations representing the highest level of commitment in orthodontics. Dr. Corvani and Dr. Lasch are among the few orthodontists who completed additional training to achieve board certification and are the <strong>only board certified orthodontists in Harlow County.</strong></p>
      </li>
      <li class="reason">
        <span class="reason__num">3</span>
        <h2 class="reason__title">You Have Choices</h2>
        <p class="reason__text">Our doctors have treated hundreds of beautiful smiles using Clearline aligners. Because of their years of varied experience, even more treatment options may be available to help you choose the <strong>perfect method</strong> that will fit your lifestyle.</p>
      </li>
      <li class="reason">
        <span class="reason__num">4</span>
        <h2 class="reason__title">Outstanding Online Reviews.</h2>
        <p class="reason__text">We invite you to read our <strong>Searchwise and Circlebook reviews.</strong> Allow our patients to tell you first-hand the reasons they love being a part of this orthodontic family.</p>
      </li>
      <li class="reason">
        <span class="reason__num">5</span>
        <h2 class="reason__title">Highly Trained, Experienced Staff with In-House Lab.</h2>
        <p class="reason__text">All staff members are always receiving continuing education to ensure the highest level of care. Our in-house lab ensures quality control, custom-made appliances, and quick turn-around time.</p>
      </li>
    </ol>
  </div>

  <div class="page inner-right">
    <svg class="art" viewBox="0 0 560 866" preserveAspectRatio="none">
      <defs>
        <radialGradient id="right-glow" cx="1" cy="0" r="1">
          <stop offset="0" stop-color="#cfe8f1"/>
          <stop offset=".5" stop-color="#eef7fa"/>
          <stop offset="1" stop-color="#ffffff"/>
        </radialGradient>
      </defs>
      <rect width="560" height="866" fill="url(#right-glow)"/>
    </svg>
    <ol class="reason-list">
      <li class="reason">
        <span class="reason__num">6</span>
        <h2 class="reason__title">State of the Art Technology</h2>
        <p class="reason__text">We use digital x-rays with the latest equipment to ensure minimal radiation. Our imaging is capable of 3D CT scanning for precise diagnosis. We have an intraoral scanner and 3D printing access to avoid putty impressions.</p>
      </li>
      <li class="reason">
        <span class="reason__num">7</span>
        <h2 class="reason__title">Flexible Appointments</h2>
        <p class="reason__text">We're available when you need us. We offer early morning and evening appointments and work with your schedule to be available when your child is off school. Our doctors are available 24/7 and you will always speak with a real person if you need to reach us for after-hours emergencies.</p>
      </li>
      <li class="reason">
        <span class="reason__num">8</span>
        <h2 class="reason__title">Flexible Financial Plans</h2>
        <p class="reason__text">We offer a number of flexible payment options and we file your insurance for you. There are no hidden costs, fees, or unpleasant surprises. Your comfort is our priority.</p>
      </li>
      <li class="reason">
        <span class="reason__num">9</span>
        <h2 class="reason__title">The Doctors' Doctor</h2>
        <p class="reason__text">Many dentists and their families are our patients. They respect our level of knowledge and expertise enough to place their loved ones under our care.</p>
      </li>
      <li class="reason">
        <span class="reason__num">10</span>
        <h2 class="reason__title">On-Time Treatment</h2>
        <p class="reason__text">We take great pride in keeping our appointments on time as well as completing treatment on time. Over 95% of our patients finish their treatment on time.</p>
      </li>
      <li class="reason">
        <span class="reason__num">11</span>
        <h2 class="reason__title">Top of the Line Materials</h2>
        <p class="reason__text">We use the highest quality brackets that are less noticeable, more hygienic, easier to keep clean, more comfortable, and engineered with pre-packaged and precoated adhesive, creating an environment that minimizes human error and maximizes performance.</p>
      </li>
    </ol>
  </div>

  <div class="fold-shadow"></div>
</section>

</body>
</html>
```